Varbek - Nutritious Snacks and Desserts

We need a creative e-commerce website in which all features--buttons, background, etc.--convey our message: We sell delicious, nutritious snacks and desserts that most closely comply with the paleo diet guidelines. Our first product is Brunavo®--raw, vegan, paleo chocolate balls that are made of dates, coconut, and cocoa. Our products are organic, raw, irresistible and nutritious. We have several versions of Brunavo® in development, as well as mousse, ice cream, and crackers. Our mission is to purvey basic healthy foods. Our motto is, "Fuel for the Daily Trail-Seeker(tm)."

Target Market(s)

Health-conscious professionals who tend to shop at health food stores. Our products also meet the requirements of a gluten-free diet; and they also don't contain refined sugar, so shoppers with gluten and possibly sugar issues are incidental customers.

Industry/Entity Type

Health Product

Coding

Coded - Design and coding required

Number of Pages Required

5+ page

Colors

Designer to choose colors to be used in the design.

Requirements
Must have
• We need at least a home page, a products page, an about-us page, a contact page, and a shopping cart page. We would like to be able to add products on our own later. We should be able to handle some basic coding, especially if it's just a matter of copying and modifying product pages. We would also like the ability in the future to add blogging pages, allowing us to write articles about health food and healthy lifestyle, thus attracting web-traffic (SEO).
• Other features we would like to have:
• Product photo slider on the hopepage
• Back-to-top button at the bottom of the home page
• Make sure the site is mobile-compatible
• A search bar at the top of the homepage
• "Create an account" and "Previous orders"--allowing customers to see their previous orders and reorder what they purchased in the past.
Nice to have
• We would like to convey the paleo theme without actually stating it anywhere. We'll add text as necessary, according to the page layout; you can use ipsum lorem for purpose of demonstration.

```html
<!DOCTYPE html>
<html lang="en">
<head>
<meta charset="utf-8">
<title>Varbek – Nutritious Snacks and Desserts</title>
<link href="https://fonts.googleapis.com/css2?family=Prata&family=Lora:wght@400;700&display=swap" rel="stylesheet">
<style>
:root{
  --leaf:#7cc21b;
  --leaf-bright:#8fd11f;
  --grass:#4f9e0a;
  --grass-deep:#2b8000;
  --forest:#2d4a06;
  --forest-card:#2f5406;
  --ink:#2b3a12;
  --text:#444;
  --paper:#f3f3f0;
  --white:#fff;
  --head:"Prata",serif;
  --body:"Lora",serif;
}
*{margin:0;padding:0;box-sizing:border-box}
html,body{width:1200px;height:3593px;overflow:hidden}
body{position:relative;font-family:var(--body);color:var(--text);background:var(--white)}
.abs{position:absolute}
.center{left:0;width:1200px;text-align:center}
.btn{position:absolute;display:flex;align-items:center;justify-content:center;border-radius:22px;font-family:var(--body);font-size:15px;color:var(--white)}
.btn-leaf{background:var(--leaf)}
.btn-forest{background:var(--forest)}
h1,h2{font-family:var(--head);font-weight:400}

/* hero */
.hero{position:absolute;left:0;top:0;width:1200px;height:628px;background:linear-gradient(160deg,#6b4a2e 0%,#5e7b2c 22%,#a63a2a 45%,#c98b86 60%,#b7b9bd 80%,#8a6b48 100%)}
.hero-shade{position:absolute;inset:0;background:linear-gradient(rgba(40,25,10,.55),rgba(0,0,0,.15) 20%,rgba(0,0,0,.1))}
.nav a{position:absolute;top:58px;font-size:15px;color:var(--white);text-decoration:none}
.nav .active{border-bottom:2px solid var(--leaf);padding-bottom:4px}
.phone{position:absolute;top:12px;left:962px;font-size:15px;color:var(--white);display:flex;align-items:center;gap:8px}
.cart{position:absolute;left:1056px;top:44px;width:40px;height:40px;border-radius:50%;border:2px solid var(--leaf);display:flex;align-items:center;justify-content:center}
.brand-disc{position:absolute;left:488px;top:-112px;width:224px;height:224px;border-radius:50%;background:var(--white);display:flex;align-items:flex-end;justify-content:center;padding-bottom:36px}
.brand-name{font-family:var(--head);font-size:30px;color:var(--grass);letter-spacing:1px}
.hero-title{top:270px;font-size:60px;line-height:66px;color:var(--white);text-shadow:0 2px 6px rgba(0,0,0,.45)}
.dots{position:absolute;top:575px;left:580px;display:flex;gap:12px}
.dots i{width:8px;height:8px;border-radius:50%;background:rgba(255,255,255,.6)}
.dots i:first-child{background:var(--white)}

/* welcome */
.welcome{position:absolute;left:0;top:628px;width:1200px;height:373px;background:linear-gradient(180deg,var(--grass) 0%,var(--grass-deep) 100%);color:var(--white);text-align:center}
.welcome h2{margin-top:62px;font-size:40px}
.welcome p{margin:36px auto 0;width:820px;font-size:15px;line-height:27px}
.welcome .bold{margin-top:12px;font-size:21px}

/* about */
.section-title{font-size:42px;color:var(--ink)}
.feature{position:absolute;text-align:center;font-size:15px;color:var(--ink);width:160px}
.about-copy{top:1628px;left:250px;width:700px;font-size:12.5px;line-height:20px;text-align:center;color:#555}
.product-disc{position:absolute;border-radius:50%;background:radial-gradient(circle,#6d4a2e 0 30%,#b99a74 31% 100%);border:10px solid var(--leaf)}

/* products */
.products{position:absolute;left:0;top:1844px;width:1200px;height:671px;background:var(--paper)}
.item{position:absolute;width:300px;text-align:center}
.item h3{font-family:var(--body);font-weight:400;font-size:19px;color:var(--ink)}
.item p{margin:8px auto 0;width:230px;font-size:12.5px;line-height:18px}
.item .price{margin-top:14px;font-size:30px;color:var(--ink)}
.item .btn{position:relative;margin:10px auto 0;width:156px;height:30px;font-size:14px}

/* blog */
.card{position:absolute;top:2658px;width:340px;height:463px;background:var(--forest-card);text-align:center;color:var(--white)}
.card.featured{background:linear-gradient(180deg,var(--leaf) 0%,var(--grass) 100%)}
.card .photo{height:247px}
.date{position:absolute;left:122px;top:199px;width:96px;height:96px;border-radius:50%;background:var(--forest);border:3px solid var(--leaf);display:flex;flex-direction:column;align-items:center;justify-content:center;font-family:var(--head);font-size:22px;line-height:22px}
.date small{font-size:11px;font-family:var(--body)}
.card .by{margin-top:60px;font-size:10px;font-weight:700}
.card .by span{font-family:var(--head);font-size:15px;font-weight:400;color:#d9f5a0}
.card p{margin:12px auto 0;width:270px;font-size:16px;line-height:22px}
.card .btn{position:relative;margin:14px auto 0;width:96px;height:26px;font-size:11px}
.card .socials{display:flex;gap:16px;justify-content:center;margin-top:16px}
.card .socials i{width:8px;height:8px;border-radius:50%;background:var(--white)}
.pager{position:absolute;top:3166px;width:30px;height:30px;border-radius:50%;border:2px solid var(--ink);display:flex;align-items:center;justify-content:center}

/* footer */
.footer{position:absolute;left:0;top:3238px;width:1200px;height:355px;background:linear-gradient(180deg,var(--grass) 0%,var(--grass-deep) 100%);color:var(--white)}
.foot-col{position:absolute;top:56px;font-size:12px;line-height:24px}
.foot-col h4{font-family:var(--body);font-weight:400;font-size:16px;margin-bottom:12px}
.newsletter{left:903px;top:60px;width:247px;height:40px;background:var(--forest);font-size:14px;gap:10px}
.social-row{position:absolute;left:908px;top:124px;display:flex;gap:8px}
.social-row i{width:30px;height:30px;border-radius:50%;border:2px solid var(--white)}
.pay-row{position:absolute;left:905px;top:186px;display:flex;gap:6px}
.pay-row i{width:42px;height:26px;border-radius:3px;background:var(--white)}
.copyright{position:absolute;left:0;top:304px;width:1200px;padding-top:16px;border-top:1px solid rgba(255,255,255,.25);text-align:center;font-size:11px}
</style>
</head>
<body>

<!-- Hero -->
<section class="hero" role="img" aria-label="Photograph of fresh vegetables, fruit, raw meat and fish on a wooden table">
  <div class="hero-shade"></div>
</section>
<nav class="nav">
  <a class="active" style="left:175px">Home</a>
  <a style="left:255px">About Us</a>
  <a style="left:358px">Products</a>
  <a style="left:785px">Blog</a>
  <a style="left:860px">Faqs</a>
  <a style="left:945px">Contact Us</a>
</nav>
<div class="phone">
  <svg width="14" height="14" viewBox="0 0 24 24"><path fill="#8fd11f" d="M6.6 10.8a15 15 0 0 0 6.6 6.6l2.2-2.2c.3-.3.7-.4 1-.2 1.1.4 2.3.6 3.6.6.6 0 1 .4 1 1V20c0 .6-.4 1-1 1A17 17 0 0 1 3 4c0-.6.4-1 1-1h3.5c.6 0 1 .4 1 1 0 1.3.2 2.5.6 3.6.1.3 0 .7-.2 1z"/></svg>
  1-555-010-4821
</div>
<div class="cart">
  <svg width="20" height="20" viewBox="0 0 24 24" fill="none" stroke="#8fd11f" stroke-width="2"><path d="M5 8h14l-1 12H6z"/><path d="M9 8V6a3 3 0 0 1 6 0v2"/></svg>
</div>
<div class="brand-disc"><span class="brand-name">Varbek</span></div>
<h1 class="abs center hero-title">Fuel for the Daily<br>Trail-Seeker™</h1>
<a class="btn btn-leaf" style="left:495px;top:434px;width:210px;height:42px">Learn More</a>
<div class="dots"><i></i><i></i><i></i></div>

<!-- Welcome -->
<section class="welcome">
  <h2>Welcome to Varbek Foods</h2>
  <p>Our products are raw, organic, vegan, gluten-free, dairy-free, fiber-rich, nutrient-dense, antioxidant-rich real foods with no preservatives, no added sugar, and no artificial or plant-based sweeteners.</p>
  <p class="bold">And they are irresistibly scrumptious!</p>
  <a class="btn btn-forest" style="left:493px;top:260px;width:214px;height:42px">Learn More</a>
</section>

<!-- About -->
<h2 class="abs center section-title" style="top:1040px">About Us</h2>
<svg class="abs" style="left:300px;top:1120px" width="600" height="600" viewBox="0 0 600 600">
  <path d="M48 305 A263 263 0 0 1 552 305" fill="none" stroke="#d7ecb3" stroke-width="2"/>
  <circle cx="300" cy="305" r="158" fill="none" stroke="#cfe99f" stroke-width="3"/>
  <!-- raw -->
  <circle cx="300" cy="42" r="30" fill="#fff" stroke="#7cc21b" stroke-width="3"/>
  <path d="M300 58 v-18 M300 44 c-10 0 -16-6 -16-16 c10 0 16 6 16 16 c0-10 6-16 16-16 c0 10 -6 16 -16 16" fill="none" stroke="#7cc21b" stroke-width="3"/>
  <!-- organic -->
  <path d="M30 208 v46 M22 208 v14 c0 6 16 6 16 0 v-14 M55 208 c10 0 10 20 0 20 v26" fill="none" stroke="#7cc21b" stroke-width="3"/>
  <path d="M42 248 c14-16 32-10 34 4 c-14 14 -30 10 -34 -4z" fill="none" stroke="#7cc21b" stroke-width="3"/>
  <!-- irresistible -->
  <rect x="530" y="212" width="40" height="40" fill="none" stroke="#7cc21b" stroke-width="3"/>
  <path d="M538 212 l6-14 M562 212 l-6-14 M550 240 c-10-8 -6-16 0-12 c6-4 10 4 0 12" fill="none" stroke="#7cc21b" stroke-width="3"/>
</svg>
<div class="feature" style="left:520px;top:1212px">Raw</div>
<div class="feature" style="left:258px;top:1428px">Organic</div>
<div class="feature" style="left:774px;top:1414px;line-height:20px">Irresistible<br>&amp; Nutritious.</div>
<div class="product-disc" role="img" aria-label="Product photo of a Brunavo chocolate ball package" style="left:468px;top:1293px;width:264px;height:264px"></div>
<p class="abs about-copy">Sed ut perspiciatis unde omnis iste natus error sit voluptatem accusantium doloremque laudantium, totam rem aperiam, eaque ipsa quae ab illo inventore veritatis et quasi architecto beatae vitae dicta sunt explicabo. Nemo enim ipsam voluptatem quia voluptas sit aspernatur aut odit aut fugit, sed quia consequuntur magni dolores eos qui ratione voluptatem sequi nesciunt.</p>
<a class="btn btn-forest" style="left:493px;top:1740px;width:214px;height:42px">Read More</a>

<!-- Products -->
<section class="products">
  <h2 class="abs center section-title" style="top:68px">Product</h2>
  <div class="product-disc" role="img" aria-label="Brunavo mousse package" style="left:115px;top:174px;width:250px;height:250px"></div>
  <div class="product-disc" role="img" aria-label="Brunavo ice cream package" style="left:475px;top:174px;width:250px;height:250px"></div>
  <div class="product-disc" role="img" aria-label="Brunavo crackers package" style="left:840px;top:174px;width:250px;height:250px"></div>
  <div class="item" style="left:90px;top:442px"><h3>Mousse</h3><p>Sed ut perspiciatis unde omnis iste natus error sit voluptatem</p><div class="price">$6.00</div><a class="btn btn-forest">View Details</a></div>
  <div class="item" style="left:450px;top:442px"><h3>Ice Cream</h3><p>Sed ut perspiciatis unde omnis iste natus error sit voluptatem</p><div class="price">$10.00</div><a class="btn btn-forest">View Details</a></div>
  <div class="item" style="left:815px;top:442px"><h3>Crackers</h3><p>Sed ut perspiciatis unde omnis iste natus error sit voluptatem</p><div class="price">$12.00</div><a class="btn btn-forest">View Details</a></div>
</section>

<!-- Blog -->
<h2 class="abs center section-title" style="top:2562px">Blog</h2>
<article class="card featured" style="left:67px">
  <div class="photo" role="img" aria-label="Photo of a shredded red cabbage salad in a wooden bowl" style="background:linear-gradient(135deg,#7a3a5c,#a8567a 50%,#6b4a2e)"></div>
  <div class="date">Jan<br>31th<small>2018</small></div>
  <div class="by">Posted By <span>Varbek</span></div>
  <p>Sed ut perspiciatis unde omnis iste natus error sit voluptatem</p>
  <a class="btn btn-forest">Read More</a>
  <div class="socials"><i></i><i></i><i></i><i></i></div>
</article>
<article class="card" style="left:434px">
  <div class="photo" role="img" aria-label="Photo of hands holding a bowl of raspberries" style="background:linear-gradient(135deg,#c8cfd8,#9fb2c9 40%,#c23a4a 70%,#8aa0bd)"></div>
  <div class="date">Jan<br>31th<small>2018</small></div>
  <div class="by">Posted By <span>Varbek</span></div>
  <p>Sed ut perspiciatis unde omnis iste natus error sit voluptatem</p>
  <a class="btn btn-leaf">Read More</a>
  <div class="socials"><i></i><i></i><i></i><i></i></div>
</article>
<article class="card" style="left:798px">
  <div class="photo" role="img" aria-label="Photo of a spinach and orange salad on a yellow plate" style="background:linear-gradient(135deg,#e8e6df,#5f8a3a 45%,#e5c23a 70%,#b9c4d2)"></div>
  <div class="date">Jan<br>31th<small>2018</small></div>
  <div class="by">Posted By <span>Varbek</span></div>
  <p>Sed ut perspiciatis unde omnis iste natus error sit voluptatem</p>
  <a class="btn btn-leaf">Read More</a>
  <div class="socials"><i></i><i></i><i></i><i></i></div>
</article>
<div class="pager" style="left:562px"><svg width="12" height="12" viewBox="0 0 12 12"><path d="M8 2 4 6l4 4" fill="none" stroke="#2b3a12" stroke-width="2"/></svg></div>
<div class="pager" style="left:606px;border-color:var(--leaf)"><svg width="12" height="12" viewBox="0 0 12 12"><path d="M4 2l4 4-4 4" fill="none" stroke="#2b3a12" stroke-width="2"/></svg></div>

<!-- Footer -->
<footer class="footer">
  <div class="abs" style="left:104px;top:44px;width:70px;height:70px;border-radius:50%;background:var(--white)"></div>
  <div class="abs" style="left:62px;top:140px;width:154px;text-align:center;font-family:var(--head);font-size:30px;letter-spacing:2px">Varbek</div>
  <div class="foot-col" style="left:263px"><h4>Menu Links</h4>Home<br>About Us<br>Products<br>Blog<br>Faqs<br>Contact Us</div>
  <div class="foot-col" style="left:441px"><h4>Support</h4>Contact<br>Returns<br>Warranty<br>Help / Shipping</div>
  <div class="foot-col" style="left:613px"><h4>Legal</h4>Privacy<br>Terms<br>Patents<br>Disclaimer</div>
  <div class="foot-col" style="left:762px"><h4>Other</h4>Account<br>Affiliate Program<br>Store Locator<br>Bag Selector</div>
  <a class="btn newsletter">
    <svg width="16" height="12" viewBox="0 0 16 12"><rect x="1" y="1" width="14" height="10" fill="none" stroke="#fff" stroke-width="1.5"/><path d="M1 1l7 6 7-6" fill="none" stroke="#fff" stroke-width="1.5"/></svg>
    Sign Up for Newsletter
  </a>
  <div class="social-row"><i></i><i></i><i></i><i></i><i></i><i></i><i></i></div>
  <div class="pay-row"><i></i><i></i><i></i><i></i><i></i></div>
  <div class="copyright">© 2018 Company Name | All Rights Reserved</div>
</footer>

</body>
</html>
```